Business Postcard to attract business listings on directory

We need a postcard that professionally and excitedly highlights the benefits of getting listed on our local business directory.

Our local business directory combines a Quarterly direct mail piece a LOCAL discount card, which means no coupons for people to remember to use, and the power of an online directory and the benefits of local SEO.

Colorful, Vector/Images and Bold text a must

Target Market(s)

Local business, all industrys that service the public, retail,food, construction,plumbing etc.

Industry/Entity Type

Business Directory

Font styles to use
Other font styles liked:
• Calibri,Verdana

Requirements
Must have
• High Quality Graphics
• Vector Icons
• Vibrant Professional Colors
• Place for my contact details
Nice to have
• Some kind of business guy, Cartoonish maybe flying or "exploding" with new business sales
Should not have
• Excessive Blank Space

```html
<!DOCTYPE html>
<html lang="en">
<head>
<meta charset="utf-8">
<title>Local Business Listing Postcard</title>
<link rel="stylesheet" href="https://fonts.googleapis.com/css2?family=Bebas+Neue&family=Open+Sans:ital,wght@1,300;1,400&family=Roboto+Condensed:wght@400&family=Montserrat:wght@400&display=swap">
<style>
  :root {
    --brand-blue: #2f3f94;
    --brand-red: #e1001f;
    --ink: #222222;
    --ink-soft: #3a3a3a;
    --paper: #ffffff;
    --panel: #efefef;
    --backdrop: #e6e6e6;
    --stamp: #cccccc;
  }
  html, body {
    margin: 0;
    padding: 0;
    width: 1200px;
    height: 1200px;
    overflow: hidden;
    background: var(--backdrop);
  }
  .postcard {
    position: absolute;
    left: 292px;
    width: 615px;
    height: 476px;
    display: block;
  }
  .postcard--front { top: 91px; }
  .postcard--back { top: 631px; }

  .headline { font-family: "Bebas Neue", "Oswald", sans-serif; font-size: 46px; fill: var(--paper); }
  .intro { font-family: "Open Sans", sans-serif; font-style: italic; font-weight: 300; font-size: 15.5px; fill: var(--ink-soft); }
  .call { font-family: "Bebas Neue", sans-serif; font-size: 50px; fill: var(--brand-red); }
  .email { font-family: "Bebas Neue", sans-serif; font-size: 29px; fill: var(--ink); }
  .web { font-family: "Montserrat", sans-serif; font-size: 18px; letter-spacing: 7px; fill: var(--paper); }
  .benefit-label { font-family: "Roboto Condensed", sans-serif; font-size: 14px; fill: var(--ink); text-anchor: middle; }

  .ring { fill: var(--paper); stroke: var(--brand-blue); stroke-width: 3; }
  .icon { fill: none; stroke: var(--brand-red); stroke-width: 2.4; stroke-linecap: round; stroke-linejoin: round; }
  .icon-solid { fill: var(--brand-red); }
  .icon-knock { font-family: "Roboto Condensed", sans-serif; font-size: 11px; fill: var(--paper); text-anchor: middle; }
</style>
</head>
<body>

<!-- Front side -->
<svg class="postcard postcard--front" viewBox="0 0 718 556" xmlns="http://www.w3.org/2000/svg">
  <defs>
    <linearGradient id="front-top" x1="0" y1="0" x2="1" y2="1">
      <stop offset="0" stop-color="#ffffff"/>
      <stop offset="1" stop-color="#ececec"/>
    </linearGradient>
    <linearGradient id="hero-scene" x1="0" y1="0" x2="0" y2="1">
      <stop offset="0" stop-color="#c9e6f6"/>
      <stop offset="0.7" stop-color="#e7f3f8"/>
      <stop offset="1" stop-color="#b9d98a"/>
    </linearGradient>
    <linearGradient id="lower-panel" x1="0" y1="0" x2="0" y2="1">
      <stop offset="0" stop-color="#f6f6f6"/>
      <stop offset="1" stop-color="#e9e9e9"/>
    </linearGradient>
    <radialGradient id="disc-fill">
      <stop offset="0" stop-color="#ffffff"/>
      <stop offset="1" stop-color="#eeeeee"/>
    </radialGradient>
  </defs>

  <rect class="front-surface" width="718" height="556" fill="url(#front-top)"/>
  <rect class="hero-illustration" x="0" y="0" width="345" height="307" fill="url(#hero-scene)"
        role="img" aria-label="Cartoon businessman in a VR headset flying over green hills"/>

  <!-- title banner -->
  <polygon class="banner-accent" points="325,61 350,61 368,131 343,131" fill="var(--brand-red)"/>
  <polygon class="banner" points="343,61 718,61 718,131 362,131" fill="var(--brand-blue)"/>
  <text class="headline" x="540" y="114" text-anchor="middle">Local Business Listing</text>

  <text class="intro">
    <tspan x="333" y="181">Get found where YOUR shoppers are searching.</tspan>
    <tspan x="333" y="203">Shoppers are increasingly turning to the web,</tspan>
    <tspan x="333" y="224">according to MarketPulse's 5th Annual Local Search</tspan>
    <tspan x="333" y="246">Usage Study. Shoppers are SEARCHING locally to</tspan>
    <tspan x="333" y="267">buy in-store and then deciding to purchase.</tspan>
  </text>

  <!-- lower panel with red rule -->
  <polygon class="contact-panel" points="0,318 322,318 346,344 718,344 718,522 0,522" fill="url(#lower-panel)"/>
  <polygon class="red-rule" points="0,307 330,307 352,333 718,333 718,345 346,345 322,319 0,319" fill="var(--brand-red)"/>

  <text class="call" x="42" y="399">Call: 123.456.78</text>
  <text class="email" x="44" y="441">Email: info@website.com</text>

  <!-- footer bands -->
  <polygon class="footer-red" points="345,522 718,522 718,556 385,556" fill="var(--brand-red)"/>
  <polygon class="footer-blue" points="0,478 318,478 386,556 0,556" fill="var(--brand-blue)"/>
  <text class="web" x="46" y="523">www.website.com</text>

  <!-- feature discs -->
  <circle class="disc" cx="427" cy="403" r="80" fill="url(#disc-fill)" stroke="var(--brand-blue)" stroke-width="6"/>
  <circle cx="427" cy="403" r="66" fill="#f1f1f1" role="img" aria-label="Illustration of a hand holding a shopping bag"/>
  <circle class="disc" cx="603" cy="403" r="80" fill="url(#disc-fill)" stroke="var(--brand-blue)" stroke-width="6"/>
  <circle cx="603" cy="403" r="66" fill="#f6dcd8" role="img" aria-label="Illustration of a red shopping bag bursting with product icons"/>
</svg>

<!-- Back side -->
<svg class="postcard postcard--back" viewBox="0 0 718 556" xmlns="http://www.w3.org/2000/svg">
  <defs>
    <linearGradient id="back-panel" x1="0" y1="0" x2="1" y2="0">
      <stop offset="0" stop-color="#f4f4f4"/>
      <stop offset="1" stop-color="#e6e6e6"/>
    </linearGradient>
  </defs>

  <rect width="718" height="556" fill="var(--paper)"/>
  <polygon class="benefits-panel" points="0,0 305,0 428,248 280,519 0,519" fill="url(#back-panel)"/>
  <polyline class="chevron-red" points="308,0 430,248 283,519" fill="none" stroke="var(--brand-red)" stroke-width="7"/>
  <polyline class="chevron-blue" points="322,0 444,248 297,519" fill="none" stroke="var(--brand-blue)" stroke-width="7"/>
  <rect class="footer-band" x="0" y="519" width="718" height="37" fill="var(--brand-red)"/>
  <rect class="stamp-box" x="619" y="26" width="64" height="64" fill="var(--stamp)"/>

  <!-- Row 1 -->
  <g class="benefit">
    <circle class="ring" cx="86" cy="76" r="30"/>
    <rect class="icon-solid" x="66" y="73" width="17" height="8" rx="2"/>
    <path class="icon-solid" d="M69 73 l3 -5 h8 l3 5z"/>
    <rect class="icon-solid" x="89" y="73" width="17" height="8" rx="2"/>
    <path class="icon-solid" d="M92 73 l3 -5 h8 l3 5z"/>
    <rect class="icon-solid" x="76" y="80" width="20" height="9" rx="2"/>
    <path class="icon-solid" d="M79 80 l3 -5 h8 l3 5z"/>
    <text class="benefit-label"><tspan x="80" y="134">MORE</tspan><tspan x="80" y="153">FOOT</tspan><tspan x="80" y="172">TRAFFIC</tspan></text>
  </g>
  <g class="benefit">
    <circle class="ring" cx="182" cy="76" r="30"/>
    <rect class="icon-solid" x="166" y="66" width="32" height="22" rx="2"/>
    <path d="M166 67 l16 12 l16 -12" fill="none" stroke="var(--paper)" stroke-width="2"/>
    <circle cx="182" cy="74" r="4" fill="none" stroke="var(--paper)" stroke-width="1.6"/>
    <text class="benefit-label"><tspan x="177" y="134">Quarterly Mailing</tspan><tspan x="177" y="153">To 10,000 local</tspan><tspan x="177" y="172">shoppers</tspan></text>
  </g>
  <g class="benefit">
    <circle class="ring" cx="289" cy="76" r="30"/>
    <rect class="icon" x="277" y="60" width="24" height="32" rx="3"/>
    <rect class="icon" x="281" y="65" width="16" height="22" rx="1"/>
    <text class="benefit-label"><tspan x="281" y="134">Desktop &amp; Mobile</tspan><tspan x="281" y="153">optimized</tspan><tspan x="281" y="172">online listing</tspan></text>
  </g>

  <!-- Row 2 -->
  <g class="benefit">
    <circle class="ring" cx="86" cy="237" r="30"/>
    <rect class="icon" x="74" y="222" width="15" height="21"/>
    <rect class="icon" x="82" y="229" width="15" height="22" fill="var(--paper)"/>
    <text class="benefit-label"><tspan x="84" y="298">Show up in</tspan><tspan x="84" y="317">Search Engine</tspan><tspan x="84" y="336">Results</tspan></text>
  </g>
  <g class="benefit">
    <circle class="ring" cx="184" cy="237" r="30"/>
    <path class="icon-solid" d="M174 221 h20 v31 l-10 -7 l-10 7z"/>
    <text class="icon-knock" x="184" y="241">S</text>
    <text class="benefit-label"><tspan x="186" y="298">List Active</tspan><tspan x="186" y="317">Coupons</tspan><tspan x="186" y="336">&amp; Deals</tspan></text>
  </g>
  <g class="benefit">
    <circle class="ring" cx="274" cy="237" r="30"/>
    <path class="icon" d="M258 247 l12 -12 M265 232 h6 v6 M268 247 l12 -12 M275 232 h6 v6"/>
    <text class="benefit-label"><tspan x="279" y="298">Connect</tspan><tspan x="279" y="317">Direct With</tspan><tspan x="279" y="336">Shoppers</tspan></text>
  </g>

  <!-- Row 3 -->
  <g class="benefit">
    <circle class="ring" cx="91" cy="389" r="30"/>
    <path class="icon-solid" d="M81 373 h20 v31 l-10 -7 l-10 7z"/>
    <text class="icon-knock" x="91" y="393">S</text>
    <text class="benefit-label"><tspan x="91" y="444">Support Local</tspan><tspan x="91" y="463">Shoppers with the</tspan><tspan x="91" y="482">LOCAL Discount Card</tspan></text>
  </g>
  <g class="benefit">
    <circle class="ring" cx="202" cy="389" r="30"/>
    <circle class="icon" cx="198" cy="393" r="9" stroke-width="4" stroke-dasharray="4 3"/>
    <circle class="icon" cx="198" cy="393" r="4"/>
    <circle class="icon" cx="211" cy="379" r="6" stroke-width="3" stroke-dasharray="3 2"/>
    <text class="benefit-label"><tspan x="206" y="444">Dedicated Account</tspan><tspan x="206" y="463">Manager Handles</tspan><tspan x="206" y="482">everything for you</tspan></text>
  </g>
</svg>

</body>
</html>
```